Unique Elegant Stationary Set

Prepare a unique eye catching stationary set consisting of :
(1) Letterhead
(2) A3 Envelope
(3) Business Card
(4) Email Signature Banner

Package to be elegant, modern, and designers not only to think of design or colors but also materials could make a big difference, embossing, debossing, glossy, matt ....etc.

I attached both our new logos (Stacked or Linear) noting you may use any of them but you cant modify anything in the logos. Also attached our final draft portfolio to see what type of projects we work on and i also have here a glimmerboard page link showing the direction we want: https://www.glimmerboard.example/dorvanmelik/business-card-design/

Target Market(s)

VVIP / Elite Developers

Industry/Entity Type

Architecture

Font styles to use
Sans Serif
Other font styles liked:
• unitext

Requirements
Should not have
• too many colors, or being busy in general. We want something pleasing to the eye

```html
<!DOCTYPE html>
<html lang="en">
<head>
<meta charset="utf-8">
<title>Kelvar Atelier — Stationery Set</title>
<link rel="stylesheet" href="https://fonts.googleapis.com/css2?family=Montserrat:wght@400;600&display=swap">
<style>
  :root {
    --canvas: #f2f2f4;
    --paper: #e7e7e8;
    --panel: #e9e9ea;
    --edge-light: #f6f6f7;
    --edge-dark: #c9c9cb;
    --brand-red: #c32129;
    --ink: #3a3a3c;
    --shadow: rgba(0,0,0,0.35);
  }
  * { box-sizing: border-box; margin: 0; padding: 0; }
  html, body { width: 1200px; height: 1059px; overflow: hidden; background: var(--canvas); }
  body { position: relative; font-family: "Montserrat", sans-serif; color: var(--ink); }

  .sheet {
    position: absolute;
    background: var(--paper);
    box-shadow: 4px 5px 6px var(--shadow);
  }
  .panel {
    position: absolute;
    background: var(--panel);
    border-top: 1px solid var(--edge-light);
    border-left: 1px solid var(--edge-light);
    border-bottom: 1.5px solid var(--edge-dark);
    border-right: 1.5px solid var(--edge-dark);
    display: flex;
    align-items: center;
  }
  .wordmark {
    color: var(--brand-red);
    font-weight: 600;
    white-space: nowrap;
    display: flex;
    align-items: center;
    letter-spacing: 0.02em;
  }
  .wordmark .mark-square {
    display: inline-block;
    background: var(--brand-red);
    margin-left: 0.25em;
    width: 0.3em;
    height: 0.3em;
    align-self: flex-end;
    margin-bottom: 0.25em;
  }
  .contact-list { list-style: none; font-size: 7.5px; line-height: 12.5px; }
  .contact-list li { display: flex; align-items: center; gap: 8px; }
  .icon { width: 7px; height: 7px; fill: var(--brand-red); flex: none; }

  /* Letterhead */
  .letterhead { left: 114px; top: 75px; width: 453px; height: 641px; }
  .letterhead .logo-panel { left: 0; top: 34px; width: 250px; height: 56px; padding-left: 34px; border-left: none; }
  .letterhead .logo-panel .wordmark { font-size: 22px; }
  .letterhead-footer {
    position: absolute; left: 0; top: 583px; width: 453px; height: 24px;
    border-top: 1px solid var(--edge-light); border-bottom: 1.5px solid var(--edge-dark);
    display: flex; align-items: center; justify-content: center; font-size: 9px;
  }
  .letterhead-footer .item { display: flex; align-items: center; gap: 9px; padding: 0 8px; }
  .letterhead-footer .item + .item { border-left: 1px solid var(--edge-dark); }
  .letterhead-footer .icon { width: 8px; height: 8px; }

  /* Business card front */
  .card-front { left: 720px; top: 78px; width: 350px; height: 200px; }
  .card-front .logo-panel { left: 0; top: 130px; width: 193px; height: 45px; padding-left: 25px; border-left: none; }
  .card-front .logo-panel .wordmark { font-size: 15px; }
  .card-front .contact-panel { left: 218px; top: 130px; width: 132px; height: 50px; padding-left: 8px; border-right: none; border-bottom: none; }

  /* Business card back */
  .card-back { left: 720px; top: 312px; width: 350px; height: 200px; }
  .card-back .logo-panel {
    left: 111px; top: 76px; width: 239px; height: 99px; border-right: none;
    flex-direction: column; justify-content: center; align-items: flex-start; padding-left: 17px;
  }
  .card-back .stack-name { color: var(--brand-red); font-weight: 600; font-size: 40px; line-height: 1; letter-spacing: 0.02em; }
  .card-back .stack-sub { color: var(--brand-red); font-weight: 600; font-size: 15px; letter-spacing: 0.72em; margin-top: 6px; }

  /* DL envelope */
  .envelope-dl { left: 91px; top: 769px; width: 501px; height: 201px; }
  .envelope-dl .logo-panel { left: 0; top: 118px; width: 228px; height: 51px; padding-left: 32px; border-left: none; }
  .envelope-dl .logo-panel .wordmark { font-size: 17px; }
  .envelope-dl .contact-panel { left: 367px; top: 118px; width: 134px; height: 51px; padding-left: 8px; border-right: none; border-bottom: none; }

  /* Large envelope */
  .envelope-large { left: 642px; top: 558px; width: 506px; height: 426px; }
  .envelope-large .flap { position: absolute; left: 0; top: 0; width: 506px; height: 74px; }
  .envelope-large .contact-panel {
    left: 28px; top: 337px; width: 208px; height: 58px; padding-left: 13px;
    border-right: none; border-bottom: none; font-size: 6.3px;
  }
  .address-grid { display: grid; grid-template-columns: auto auto; column-gap: 6px; row-gap: 4px; align-items: center; }
  .address-grid .item { display: flex; align-items: center; gap: 6px; white-space: nowrap; }
  .address-grid .item.split { padding-left: 6px; border-left: 1px solid var(--brand-red); }
  .address-grid .address { font-size: 4.6px; line-height: 6px; }
  .envelope-large .icon { width: 6px; height: 6px; }
  .envelope-large .logo-panel { left: 288px; top: 337px; width: 218px; height: 60px; padding-left: 15px; border-right: none; }
  .envelope-large .logo-panel .wordmark { font-size: 17px; }
</style>
</head>
<body>

<svg width="0" height="0" style="position:absolute" aria-hidden="true">
  <symbol id="i-phone" viewBox="0 0 10 10"><path d="M2.2 0.6l1.6 1.8-0.9 1.2c0.6 1.3 1.5 2.2 2.8 2.8l1.2-0.9 1.8 1.6-1 1.6C4.8 8.6 1.4 5.2 0.6 1.6z"/></symbol>
  <symbol id="i-mail" viewBox="0 0 10 10"><path d="M0.5 2h9v6h-9z M1.2 2.6l3.8 2.9 3.8-2.9" stroke="#e7e7e8" stroke-width="0.7"/></symbol>
  <symbol id="i-globe" viewBox="0 0 10 10"><circle cx="5" cy="5" r="4.5"/><path d="M0.5 5h9M5 0.5c-2.4 2.6-2.4 6.4 0 9M5 0.5c2.4 2.6 2.4 6.4 0 9" stroke="#e7e7e8" stroke-width="0.6" fill="none"/></symbol>
  <symbol id="i-pin" viewBox="0 0 10 10"><path d="M5 0.3a3.4 3.4 0 0 1 3.4 3.4C8.4 6 5 9.7 5 9.7S1.6 6 1.6 3.7A3.4 3.4 0 0 1 5 0.3z"/><circle cx="5" cy="3.7" r="1.3" fill="#e7e7e8"/></symbol>
</svg>

<section class="sheet letterhead" aria-label="Letterhead">
  <div class="panel logo-panel"><span class="wordmark">KELVAR ATELIER<span class="mark-square"></span></span></div>
  <footer class="letterhead-footer">
    <span class="item"><svg class="icon"><use href="#i-phone"/></svg>+00 123 456789</span>
    <span class="item"><svg class="icon"><use href="#i-mail"/></svg>contact@kelvarmail.example</span>
    <span class="item"><svg class="icon"><use href="#i-globe"/></svg>www.yourwebsite.com</span>
  </footer>
</section>

<section class="sheet card-front" aria-label="Business card front">
  <div class="panel logo-panel"><span class="wordmark">KELVAR ATELIER<span class="mark-square"></span></span></div>
  <div class="panel contact-panel">
    <ul class="contact-list">
      <li><svg class="icon"><use href="#i-phone"/></svg>+00 123 456789</li>
      <li><svg class="icon"><use href="#i-mail"/></svg>contact@kelvarmail.example</li>
      <li><svg class="icon"><use href="#i-globe"/></svg>www.yourwebsite.com</li>
    </ul>
  </div>
</section>

<section class="sheet card-back" aria-label="Business card back">
  <div class="panel logo-panel">
    <span class="stack-name">KELVAR</span>
    <span class="stack-sub">ATELIER</span>
  </div>
</section>

<section class="sheet envelope-dl" aria-label="DL envelope">
  <div class="panel logo-panel"><span class="wordmark">KELVAR ATELIER<span class="mark-square"></span></span></div>
  <div class="panel contact-panel">
    <ul class="contact-list">
      <li><svg class="icon"><use href="#i-phone"/></svg>+00 123 456789</li>
      <li><svg class="icon"><use href="#i-mail"/></svg>contact@kelvarmail.example</li>
      <li><svg class="icon"><use href="#i-globe"/></svg>www.yourwebsite.com</li>
    </ul>
  </div>
</section>

<section class="sheet envelope-large" aria-label="Large envelope">
  <svg class="flap" viewBox="0 0 506 74" aria-hidden="true">
    <path d="M0 0 L18 58 Q24 72 40 72 L466 72 Q482 72 488 58 L506 0 Z" fill="#e9e9ea" stroke="#cfcfd1" stroke-width="1.2"/>
  </svg>
  <div class="panel contact-panel">
    <div class="address-grid">
      <span class="item"><svg class="icon"><use href="#i-phone"/></svg>+00 123 456789</span>
      <span class="item split"><svg class="icon"><use href="#i-mail"/></svg>contact@kelvarmail.example</span>
      <span class="item"><svg class="icon"><use href="#i-globe"/></svg>www.yourwebsite.com</span>
      <span class="item split"><svg class="icon"><use href="#i-pin"/></svg><span class="address">123 Anywhere St. Any City,<br>ST 12345</span></span>
    </div>
  </div>
  <div class="panel logo-panel"><span class="wordmark">KELVAR ATELIER<span class="mark-square"></span></span></div>
</section>

</body>
</html>
```